Business Card Design and New Company Logo

I need a business card design and new company logo for a plant nursery. I will be propagating landscape plants from cuttings and growing them locally for resale, locally grown and nurtured plants for zone 5 climate. I would like a design that depicts the growth of shoots to roots .... locally grown and nurtured landscape plants. Healthy, hardy ornamental trees and shrubs for $4.97. Affordable gardening for all.
Updates
Hello Designers,
Thank you for your submissions. I am going to be out of my office until Monday. I will continue to review submitted designs when I can and posting requests for revisions when time permits on my business trip. I should have a decision next week.
Sincerely,
Marla
Sorry for my delay in choosing a design. I had some unforeseen business and personal events culminate at the same time. I will have my decision by the end of this week and update all by Friday March 21. Thank you for your design submissions and your patience.
Marla
Target Market(s)
Home owners
Industry/Entity Type
Landscape
Contact Information for Business Card
Fernwick Hollow Nursery
Marla Quenby
214 Cobble Brook Lane
Amherst, MA 01002
413-862-3094
Fernwick4Hollow@mailvale.net
Font styles to use
Look and feel
Each slider illustrates characteristics of the customer's brand and the style your logo design should communicate.

```html
<!DOCTYPE html>
<html lang="en">
<head>
<meta charset="utf-8">
<title>Fernwick Hollow Nursery — Business Card</title>
<link rel="stylesheet" href="https://fonts.googleapis.com/css2?family=Montserrat:wght@500;700&display=swap">
<style>
  :root {
    --stage: #6e7076;
    --bark: #3f1712;
    --bark-faint: #4f1e17;
    --lime: #d7e01f;
    --leaf: #2fa14a;
    --card-text: #c9d61c;
  }
  * { box-sizing: border-box; margin: 0; padding: 0; }
  html, body { width: 1200px; height: 1000px; overflow: hidden; }
  body {
    background: var(--stage);
    font-family: "Montserrat", Arial, sans-serif;
    position: relative;
  }
  .card {
    position: absolute;
    width: 630px;
    height: 360px;
    overflow: hidden;
    box-shadow: 0 8px 22px rgba(0,0,0,0.35);
  }
  .card--back {
    left: 285px;
    top: 95px;
    background: var(--bark);
  }
  .card--front {
    left: 285px;
    top: 545px;
    background: var(--lime);
  }
  .back-watermark {
    position: absolute;
    left: 40px;
    top: 10px;
    width: 560px;
    font-weight: 700;
    font-size: 74px;
    line-height: 1.05;
    color: var(--bark-faint);
    text-align: center;
  }
  .contact {
    position: absolute;
    left: 0;
    right: 0;
    top: 196px;
    text-align: center;
    color: var(--card-text);
    font-weight: 700;
    font-size: 13px;
    line-height: 1.6;
    letter-spacing: 0.02em;
  }
  .contact .caps { text-transform: uppercase; }
  .contact .email { font-weight: 500; }
  .brand {
    position: absolute;
    left: 0;
    right: 0;
    top: 118px;
    text-align: center;
    color: var(--bark);
  }
  .brand-mark {
    display: inline-block;
    width: 22px;
    height: 22px;
    border-radius: 50%;
    background: var(--leaf);
    margin-bottom: 8px;
  }
  .brand-name {
    font-weight: 700;
    font-size: 40px;
    line-height: 1.05;
  }
</style>
</head>
<body>
  <section class="card card--back" aria-label="Card back">
    <div class="back-watermark" aria-hidden="true">Fernwick<br>Hollow</div>
    <address class="contact">
      <div class="caps">Fernwick Hollow Nursery</div>
      <div class="caps">Marla Quenby 214 Cobble Brook Lane Amherst,</div>
      <div class="caps">MA 01002 413-862-3094</div>
      <div class="email">fernwick4hollow@mailvale.net</div>
    </address>
  </section>

  <section class="card card--front" aria-label="Card front">
    <div class="brand">
      <span class="brand-mark" aria-hidden="true"></span>
      <div class="brand-name">Fernwick Hollow<br>Nursery</div>
    </div>
  </section>
</body>
</html>
```